Mosk trail Website

We need a simple web page design for our businessWe procure and dispose of earthmoving construction equipmentwe also find construction equipment for our customers using our global contacts

Number of Pages Required

1 page

```html
<!DOCTYPE html>
<html lang="en">
<head>
<meta charset="utf-8">
<title>Mosk trail – Earthmoving &amp; Civil Works</title>
<link href="https://fonts.googleapis.com/css2?family=Poppins:wght@400;500;600;700&display=swap" rel="stylesheet">
<style>
:root{
  --yellow:#fbae24;
  --dark:#2d3038;
  --darker:#23262d;
  --ink:#2b2b2b;
  --muted:#6f6f6f;
  --white:#ffffff;
  --field:#5a5d65;
}
*{margin:0;padding:0;box-sizing:border-box}
html,body{width:1200px;height:2531px;overflow:hidden}
body{position:relative;font-family:'Poppins',sans-serif;color:var(--ink);background:var(--white)}
.abs{position:absolute}
.btn{position:absolute;display:flex;align-items:center;justify-content:center;font-weight:600;font-size:11px;letter-spacing:.5px;text-transform:uppercase;border-radius:3px}
.btn-yellow{background:var(--yellow);color:var(--ink)}
/* header */
.site-header{left:0;top:0;width:1200px;height:79px;background:var(--white)}
.brand{left:134px;top:14px;display:flex;align-items:center;gap:10px}
.brand-mark{width:44px;height:44px;background:var(--ink)}
.brand-name{font-weight:700;font-size:20px;line-height:22px;color:var(--ink);width:70px}
.contact-chip{display:flex;align-items:center;gap:10px;top:22px}
.chip-icon{width:22px;height:22px;border:1.5px solid var(--yellow);border-radius:50%;display:flex;align-items:center;justify-content:center}
.chip-label{font-size:9px;color:var(--muted);line-height:12px}
.chip-value{font-size:12px;font-weight:600;color:var(--ink);line-height:16px}
.main-nav{left:0;top:79px;width:1200px;height:40px;background:var(--yellow)}
.main-nav a{position:absolute;top:13px;font-size:11px;font-weight:600;color:var(--ink);text-decoration:none}
.nav-quote{left:928px;top:0;width:140px;height:40px;background:var(--dark);color:var(--white);display:flex;align-items:center;justify-content:center;font-size:12px;font-weight:600}
/* hero */
.hero{left:0;top:119px;width:1200px;height:454px;background:linear-gradient(180deg,#3c4549 0%,#5a5f5c 45%,#6e5650 75%,#8a6a62 100%)}
.hero-machine{left:680px;top:60px;width:440px;height:330px;background:radial-gradient(ellipse at 55% 60%,#d9a126 0%,#8c6a2a 45%,rgba(90,80,70,0) 75%)}
.hero-title{left:135px;top:152px;font-size:30px;font-weight:700;color:var(--yellow);letter-spacing:.5px}
.hero-text{left:137px;top:197px;width:540px;font-size:11.5px;line-height:22px;color:#e6e6e6}
.hero-arrow{top:190px;color:var(--white);font-size:20px}
/* welcome */
.welcome-title{left:143px;top:648px;font-size:20px;font-weight:700;color:var(--ink)}
.welcome-text{left:143px;top:692px;width:480px;font-size:11px;line-height:23px;color:var(--muted)}
.welcome-text p+p{margin-top:8px}
.welcome-accent{left:765px;top:615px;width:303px;height:283px;background:var(--yellow)}
.welcome-photo{left:688px;top:646px;width:353px;height:290px;background:linear-gradient(160deg,#3a3f52 0%,#6a5145 55%,#c9932a 100%)}
/* services */
.services{left:0;top:990px;width:1200px;height:473px;background:linear-gradient(180deg,#3a3c3e,#2f2d2a)}
.services-title{left:0;width:1200px;top:84px;text-align:center;font-size:20px;font-weight:700;color:var(--white)}
.services-text{left:270px;width:660px;top:118px;text-align:center;font-size:11px;line-height:24px;color:#e0e0e0}
.service-card{top:216px;width:296px;height:167px;border:2px solid var(--white)}
.service-label{top:398px;width:296px;text-align:center;font-size:14px;font-weight:500;color:var(--white)}
.slider-arrow{top:263px;width:34px;height:30px;background:var(--white);display:flex;align-items:center;justify-content:center;color:var(--ink);font-size:12px}
/* works */
.works-title{left:0;width:1200px;top:1500px;text-align:center;font-size:20px;font-weight:700}
.works-text{left:390px;width:420px;top:1538px;text-align:center;font-size:11px;line-height:22px;color:var(--muted)}
.work-photo{top:1616px;width:204px;height:133px}
.work-name{top:1760px;font-size:11px;font-weight:600;color:var(--ink)}
.work-desc{top:1782px;width:210px;font-size:11px;line-height:21px;color:var(--muted)}
/* cta */
.cta{left:0;top:1873px;width:1200px;height:161px;background:var(--yellow)}
.cta-title{left:136px;top:43px;font-size:19px;font-weight:700;color:var(--ink)}
.cta-text{left:136px;top:80px;width:620px;font-size:11px;line-height:23px;color:var(--ink)}
.cta-btn{left:839px;top:62px;width:173px;height:50px;background:var(--white);color:var(--ink);font-size:12px}
/* footer */
.site-footer{left:0;top:2034px;width:1200px;height:497px;background:linear-gradient(180deg,#30333a,#272a30)}
.footer-heading{font-size:11px;font-weight:600;color:var(--white);letter-spacing:1px}
.field{background:var(--field);border-radius:3px;display:flex;align-items:flex-start;padding:9px 12px;gap:10px;font-size:11px;color:#e8e8e8}
.info-label{font-size:9px;color:#9a9ca2;letter-spacing:1px}
.info-value{font-size:12px;line-height:22px;color:var(--white)}
.social{width:24px;height:24px;background:#5c6068;border-radius:2px}
.copyright{left:0;width:1200px;top:456px;text-align:center;font-size:9px;color:#9a9ca2}
</style>
</head>
<body>

<header class="abs site-header">
  <div class="abs brand">
    <div class="brand-mark"></div>
    <div class="brand-name">Mosk trail</div>
  </div>
  <div class="abs contact-chip" style="left:743px">
    <span class="chip-icon"><svg width="11" height="9" viewBox="0 0 11 9"><rect x=".5" y=".5" width="10" height="8" fill="none" stroke="#fbae24"/><path d="M.5 .5 5.5 5 10.5 .5" fill="none" stroke="#fbae24"/></svg></span>
    <div><div class="chip-label">email us</div><div class="chip-value">hello@mosktrail.com</div></div>
  </div>
  <div class="abs contact-chip" style="left:951px">
    <span class="chip-icon"><svg width="11" height="11" viewBox="0 0 11 11"><path d="M2 1 4 1 5 3.5 3.6 4.6Q4.8 6.6 6.4 7.4L7.5 6 10 7V9Q9.5 10 8.5 10 1 9 1 2.5 1 1 2 1Z" fill="#fbae24"/></svg></span>
    <div><div class="chip-label">call now</div><div class="chip-value">0400 123 456</div></div>
  </div>
</header>

<nav class="abs main-nav">
  <a style="left:137px">HOME</a>
  <a style="left:221px">ABOUT US</a>
  <a style="left:315px">PROJECTS</a>
  <a style="left:413px">EQUIPMENT</a>
  <a style="left:517px">ACTIVITIES</a>
  <a style="left:618px">CLIENTS</a>
  <a style="left:704px">CONTACT US</a>
  <div class="abs nav-quote">GET A QUOTE</div>
</nav>

<section class="abs hero" role="img" aria-label="Backhoe loader lifting soil on a dusty work site under a cloudy sky">
  <div class="abs hero-machine"></div>
  <div class="abs hero-arrow" style="left:98px">&#8249;</div>
  <div class="abs hero-arrow" style="left:1084px">&#8250;</div>
  <h1 class="abs hero-title">EARTHMOVING &amp; CIVIL WORKS</h1>
  <p class="abs hero-text">Mauris volutpat nulla a enim efficitur elementum porttor at diam aliquam et elit elementum. fermentum nisl sed. pellentesque mares. Integer blandit erat bibendum pulvinar lobortis. Mauris sed turpis.</p>
  <div class="btn btn-yellow" style="left:136px;top:256px;width:140px;height:38px">KNOW MORE</div>
</section>

<section class="welcome">
  <h2 class="abs welcome-title">WELCOME TO MOSK TRAIL</h2>
  <div class="abs welcome-text">
    <p>quia non numquam eius modi tempora incidunt ut labore et dolore magnam aliquam quaerat voluptatem. Ut enim ad minima veniam. quis nostrum exercitationem ullam corporis suscipit laboriosam, nisi ut aliquid ex ea commodi consequatur? Quis autem vel eum iure reprehenderit qui in ea volup.</p>
    <p>quia non numquam eius modi tempora incidunt ut labore et dolore magnam aliquam quaerat voluptatem. Ut enim ad minima veniam. quis nostrum</p>
  </div>
  <div class="btn btn-yellow" style="left:144px;top:874px;width:108px;height:32px">READ MORE</div>
  <div class="abs welcome-accent"></div>
  <div class="abs welcome-photo" role="img" aria-label="Tracked excavator digging at dusk"></div>
</section>

<section class="abs services" role="img" aria-label="Excavator on a work site in darkened background">
  <svg class="abs" style="left:520px;top:0" width="160" height="40" viewBox="0 0 160 40"><path d="M0 0H160L130 40H30Z" fill="#ffffff"/><path d="M66 0H94L80 14Z" fill="#fbae24"/></svg>
  <h2 class="abs services-title">WE PROVIDE SERVICES</h2>
  <p class="abs services-text">quia non numquam eius modi tempora incidunt ut labore et dolore magnam aliquam quaerat voluptatem. Ut enim ad minima veniam. quis nostrum</p>
  <div class="abs slider-arrow" style="left:118px">&#8249;</div>
  <div class="abs slider-arrow" style="left:1052px;width:34px">&#8250;</div>
  <div class="abs service-card" style="left:134px;background:linear-gradient(150deg,#8a8478,#b8862e 55%,#6b6356)" role="img" aria-label="Excavator breaking rock"></div>
  <div class="abs service-card" style="left:449px;background:linear-gradient(180deg,#3f62b4,#8aa0cf 60%,#7a6a60)" role="img" aria-label="Worker beside a demolition machine under blue sky"></div>
  <div class="abs service-card" style="left:770px;background:linear-gradient(180deg,#d9d9d6,#f0efe9 50%,#55575a)" role="img" aria-label="Tipper truck loaded with recycled material"></div>
  <div class="abs service-label" style="left:134px">Excavation</div>
  <div class="abs service-label" style="left:449px">Demolition</div>
  <div class="abs service-label" style="left:770px">Site Remediation &amp; Recycling</div>
</section>

<section class="works">
  <h2 class="abs works-title">OUR WORKS</h2>
  <p class="abs works-text">Lorem ipsum dolor sit amet, consectetur adipisicing elit, sed do eiusmod tempor incididunt ut labore et dolore magna aliqua</p>
  <div class="abs work-photo" style="left:148px;background:linear-gradient(180deg,#a8b3bd,#6e665c 60%,#a39886)" role="img" aria-label="Excavator on a warehouse site"></div>
  <div class="abs work-photo" style="left:385px;background:linear-gradient(180deg,#5a86c8,#b58b3a 60%,#8a7e6c)" role="img" aria-label="Excavator removing asbestos material"></div>
  <div class="abs work-photo" style="left:614px;background:linear-gradient(180deg,#c9ccd0,#c7a33c 55%,#6f6a62)" role="img" aria-label="Excavator working on civil structures"></div>
  <div class="abs work-photo" style="left:852px;background:linear-gradient(180deg,#d8d8d4,#9a9a92 50%,#c9562a 75%,#6d6a62)" role="img" aria-label="Excavator clearing trees for infrastructure"></div>
  <div class="abs work-name" style="left:148px">WAREHOUSES</div>
  <div class="abs work-name" style="left:385px">ASBESTOS REMOVAL</div>
  <div class="abs work-name" style="left:614px">CIVIL STRUCTURES</div>
  <div class="abs work-name" style="left:852px">POWER &amp; MINING INFRASTRUCTURE</div>
  <p class="abs work-desc" style="left:148px">quia non numquam eius modi tem-pora incidunt ut labore et dolore</p>
  <p class="abs work-desc" style="left:385px">quia non numquam eius modi tem-pora incidunt ut labore et dolore</p>
  <p class="abs work-desc" style="left:614px">quia non numquam eius modi tem-pora incidunt ut labore et dolore</p>
  <p class="abs work-desc" style="left:852px">quia non numquam eius modi tem-pora incidunt ut labore et dolore</p>
</section>

<section class="abs cta">
  <h2 class="abs cta-title">READY TO WORK WITH OUR COMPANY?</h2>
  <p class="abs cta-text">Lorem ipsum dolor sit amet, consectetur adipiscing elit. Integer in condimentum risus. Fusce rutrum, leo in elementum sodales, magna eros vehicula ante, eget semper mi lectus nec ipsum.</p>
  <div class="btn cta-btn">GET A QUOTE</div>
</section>

<footer class="abs site-footer">
  <div class="abs footer-heading" style="left:178px;top:90px">SEND A MESSAGE</div>
  <div class="abs field" style="left:178px;top:126px;width:393px;height:33px"><svg width="11" height="9" viewBox="0 0 11 9"><rect width="11" height="9" fill="#e8e8e8"/><path d="M0 0 5.5 5 11 0" fill="none" stroke="#5a5d65"/></svg>name@mail.com</div>
  <div class="abs field" style="left:178px;top:183px;width:189px;height:33px"><svg width="10" height="10" viewBox="0 0 10 10"><circle cx="5" cy="3" r="2.5" fill="#e8e8e8"/><path d="M0 10Q0 6 5 6 10 6 10 10Z" fill="#e8e8e8"/></svg>Denis</div>
  <div class="abs field" style="left:384px;top:183px;width:187px;height:33px"><svg width="11" height="9" viewBox="0 0 11 9"><rect y="2" width="11" height="7" fill="#e8e8e8"/><rect x="3.5" width="4" height="3" fill="none" stroke="#e8e8e8"/></svg>Cashback<span style="margin-left:auto">&#8964;</span></div>
  <div class="abs field" style="left:178px;top:240px;width:393px;height:96px"><svg width="11" height="10" viewBox="0 0 11 10"><path d="M5.5 0C8.5 0 11 1.8 11 4S8.5 8 5.5 8L2 10 2.6 7C1 6.2 0 5.2 0 4 0 1.8 2.5 0 5.5 0Z" fill="#e8e8e8"/></svg>name@mail.com</div>
  <div class="btn btn-yellow" style="left:459px;top:360px;width:112px;height:34px;color:var(--white)">SEND</div>

  <div class="abs footer-heading" style="left:644px;top:90px">CONTACT INFORMATION</div>
  <div class="abs info-label" style="left:644px;top:126px">ADDRESS</div>
  <div class="abs info-value" style="left:644px;top:142px">Riverbend, WA<br>Quarry Rd, Unit<br>Riverbend,</div>
  <div class="abs info-label" style="left:644px;top:234px">PHONE</div>
  <div class="abs info-value" style="left:644px;top:250px">(08) 5550-1842</div>
  <div class="abs info-label" style="left:882px;top:126px">E-MAIL</div>
  <div class="abs info-value" style="left:882px;top:142px">office@mosktrail.com</div>
  <div class="abs info-label" style="left:882px;top:190px">SOCIAL LINKS</div>
  <div class="abs" style="left:882px;top:225px;display:flex;gap:4px">
    <span class="social"></span><span class="social"></span><span class="social"></span><span class="social"></span><span class="social"></span>
  </div>
  <div class="abs copyright">© Copyright 2018 mosktrail.com. All rights reserved.</div>
</footer>

</body>
</html>
```